Meridale Capital Partners - Real estate loans - need a business card with a logo

I need a logo and a business card that looks elegant - that looks as if it is a big stablish corporation - We do real estate loans, my goal is to brand myself with colors black background - gold or silver letters - some combination - Name of the company different color than the rest of the card -

```html
<!DOCTYPE html>
<html lang="en">
<head>
<meta charset="utf-8">
<title>Meridale Capital Partners – Business Card</title>
<link href="https://fonts.googleapis.com/css2?family=Arimo:wght@400;700&family=Oswald:wght@500&display=swap" rel="stylesheet">
<style>
  :root {
    --bg: #1c1c1c;
    --card: #141414;
    --card-edge: #2a2a2a;
    --gold: #c9a24a;
    --gold-light: #e0c27a;
  }
  * { margin: 0; padding: 0; box-sizing: border-box; }
  html, body { width: 1200px; height: 900px; overflow: hidden; }
  body {
    background: radial-gradient(ellipse at 60% 35%, #2b2b2b 0%, var(--bg) 60%, #0e0e0e 100%);
    font-family: "Arimo", Arial, sans-serif;
    position: relative;
  }
  .card {
    position: absolute;
    left: 320px;
    width: 560px;
    height: 320px;
    background: linear-gradient(135deg, #181818 0%, var(--card) 55%, #101010 100%);
    border: 1px solid var(--card-edge);
    box-shadow: 0 18px 40px rgba(0,0,0,0.6);
  }
  .card--front { top: 100px; }
  .card--back { top: 450px; }

  .brand {
    position: absolute;
    top: 0; left: 0; right: 0; bottom: 0;
    display: flex;
    flex-direction: column;
    align-items: center;
    justify-content: center;
    gap: 18px;
  }
  .brand__mark {
    width: 70px; height: 70px;
    background: var(--gold);
  }
  .brand__name {
    color: var(--gold);
    font-family: "Arimo", Arial, sans-serif;
    font-weight: 700;
    font-size: 26px;
    letter-spacing: 3px;
    text-transform: uppercase;
    text-align: center;
    line-height: 1.25;
  }

  .holder {
    position: absolute;
    right: 305px;
    top: 118px;
    text-align: right;
  }
  .holder__name {
    font-family: "Oswald", "Arial Narrow", sans-serif;
    font-weight: 500;
    font-size: 36px;
    letter-spacing: 1.5px;
    color: var(--gold);
    text-transform: uppercase;
    line-height: 1.1;
  }
  .holder__title {
    font-size: 17px;
    color: var(--gold-light);
    margin-top: 4px;
  }
  .divider {
    position: absolute;
    left: 278px;
    top: 100px;
    width: 2px;
    height: 118px;
    background: var(--gold);
  }
  .contact {
    position: absolute;
    left: 300px;
    top: 100px;
    color: var(--gold-light);
    font-size: 17px;
    line-height: 1.35;
    list-style: none;
  }
  .contact li { display: flex; align-items: center; gap: 6px; white-space: nowrap; }
  .contact__icon { width: 12px; height: 12px; flex: none; }
  .contact__plain { padding-left: 18px; }
</style>
</head>
<body>
  <section class="card card--front">
    <div class="brand">
      <div class="brand__mark"></div>
      <div class="brand__name">Meridale<br>Capital Partners</div>
    </div>
  </section>

  <section class="card card--back">
    <div class="holder">
      <div class="holder__name">Daniel Harper</div>
      <div class="holder__title">Founder</div>
    </div>
    <div class="divider"></div>
    <ul class="contact">
      <li class="contact__plain">418 Linden Avenue</li>
      <li class="contact__plain">Colville, WA 99114</li>
      <li>
        <svg class="contact__icon" viewBox="0 0 12 12" aria-hidden="true"><path d="M3 1 L5 3.5 L4 5 Q5 7 7 8 L8.5 7 L11 9 L9.5 11 Q4 10.5 1 3 Z" fill="none" stroke="#e0c27a" stroke-width="1"/></svg>
        555 210 4837
      </li>
      <li>
        <svg class="contact__icon" viewBox="0 0 12 12" aria-hidden="true"><rect x="1" y="2.5" width="10" height="7" fill="none" stroke="#e0c27a" stroke-width="1"/><path d="M1 2.5 L6 6.5 L11 2.5" fill="none" stroke="#e0c27a" stroke-width="1"/></svg>
        info@meridalecapital.com
      </li>
      <li>
        <svg class="contact__icon" viewBox="0 0 12 12" aria-hidden="true"><circle cx="6" cy="6" r="5" fill="none" stroke="#e0c27a" stroke-width="1"/><ellipse cx="6" cy="6" rx="2.2" ry="5" fill="none" stroke="#e0c27a" stroke-width="0.8"/><path d="M1 6 H11" stroke="#e0c27a" stroke-width="0.8"/></svg>
        www.meridalecapital.com
      </li>
      <li class="contact__plain">www.meridalecapital.com</li>
    </ul>
  </section>
</body>
</html>
```